Company or website name
- Harwood & Beale LLP
- Links to the website
- harwoodbeale-example.com
- Describe your company and organization and target audience
- lawyers and clients in the need of lawyer for defective products etc
- The design should have the following
- yes
- Other Facts

```html
<!DOCTYPE html>
<html lang="en">
<head>
<meta charset="utf-8">
<title>Harwood &amp; Beale LLP</title>
<link href="https://fonts.googleapis.com/css2?family=Cabin:wght@400;600&family=Oswald:wght@500&family=Open+Sans:wght@400;700&family=Dosis:wght@500&display=swap" rel="stylesheet">
<style>
:root{
  --orange:#f47a0c;
  --orange-light:#ffb12d;
  --blue:#0a5ba6;
  --blue-dark:#0c3f7c;
  --navy:#0b1633;
  --text:#333;
  --muted:#555;
  --line:#d9d9d9;
}
*{margin:0;padding:0;box-sizing:border-box}
html,body{width:994px;height:1200px;overflow:hidden;background:#fff}
.page{position:absolute;left:0;top:0;width:1200px;height:1448px;transform:scale(.82833);transform-origin:0 0;font-family:"Cabin",sans-serif;color:var(--text)}
.abs{position:absolute}
.topbar{left:0;top:0;width:1200px;height:47px;background:linear-gradient(#ffad2c,#f68a12)}
.topline{left:0;top:47px;width:1200px;height:8px;background:linear-gradient(#174f97,#0d3670)}
.hero{left:0;top:55px;width:1200px;height:753px;background:linear-gradient(100deg,#c9d9e6 0%,#aac3d9 30%,#7d9dbe 55%,#3c5c88 75%,#2a4370 100%)}
.logo-box{left:100px;top:0;width:283px;height:103px;background:#fff;border-radius:0 0 8px 8px;box-shadow:0 2px 6px rgba(0,0,0,.15);display:flex;align-items:center;padding-left:12px;gap:10px}
.logo-dot{width:40px;height:40px;border-radius:50%;background:var(--orange)}
.logo-name{font-family:"Cabin",sans-serif;font-weight:600;font-size:21px;color:var(--blue-dark);white-space:nowrap}
.nav{left:525px;top:0;height:47px;display:flex;list-style:none}
.nav li{font-family:"Oswald",sans-serif;font-weight:500;font-size:19px;color:#2b1a08;line-height:46px;padding:0 18px;border-right:1px solid rgba(160,80,0,.35);letter-spacing:-.3px}
.nav li:last-child{border-right:0}
.util{left:715px;top:58px;width:392px;height:44px;background:#fff;clip-path:polygon(0 0,100% 0,96% 100%,5% 100%);border-radius:0 0 10px 10px}
.search{left:760px;top:67px;width:177px;height:27px;border:1px solid #ccc;background:#fff;font-family:Arial,sans-serif;font-size:11px;color:#777;padding:6px 4px}
.search svg{position:absolute;right:5px;top:4px}
.phone{left:965px;top:70px;font-family:"Open Sans",sans-serif;font-size:16px;color:#666;display:flex;align-items:center;gap:6px}
.arrow{top:340px}
.tagline{left:566px;top:291px;width:501px;height:157px;background:var(--blue);padding:22px 12px 0 13px;box-shadow:0 2px 8px rgba(0,0,0,.3)}
.tagline h1{font-family:"Open Sans",sans-serif;font-weight:700;font-size:24px;color:#cfe6fb;margin-bottom:6px}
.tagline p{font-family:"Open Sans",sans-serif;font-size:12.5px;line-height:18px;color:#fff}
.features{left:100px;top:663px;width:1000px;height:215px;border-top:10px solid var(--blue);background:#fff;display:flex;box-shadow:0 2px 4px rgba(0,0,0,.08)}
.feature{position:relative;flex:0 0 auto;border-right:1px solid #e3e3e3;text-align:center}
.feature:last-child{border-right:0}
.feature .hex{position:absolute;left:50%;top:-38px;transform:translateX(-50%)}
.feature h2{font-family:"Cabin",sans-serif;font-weight:400;font-size:20px;color:var(--orange);margin-top:38px;padding-bottom:6px;border-bottom:1px solid #e5e5e5}
.feature p{font-size:14.5px;line-height:20px;color:#444;text-align:left;padding:4px 14px 0 17px}
.more-row{position:absolute;left:0;right:0;display:flex;justify-content:center;align-items:center}
.more-row::before,.more-row::after{content:"";width:55px;height:1px;background:#bbb}
.btn{display:inline-flex;align-items:center;gap:5px;background:linear-gradient(#1c64b3,#0b4586);color:#fff;font-size:14px;height:24px;width:65px;padding-left:6px;border-radius:2px}
.btn svg{flex:0 0 auto}
.content{left:100px;top:905px;width:1000px;height:383px;background:#fff;box-shadow:0 1px 4px rgba(0,0,0,.2)}
.main h2,.news h2{font-weight:400;font-size:22px;color:var(--orange)}
.main{left:118px;top:912px;width:624px}
.main hr{border:0;border-top:1px solid var(--line);margin:16px 4px 14px 0;width:620px}
.main p{font-size:14.6px;line-height:26px;color:#333;margin-bottom:26px}
.news{left:810px;top:912px;width:280px}
.news .date{font-family:"Dosis",sans-serif;font-weight:500;font-size:15px;color:var(--orange);margin-top:12px}
.news p{font-size:14.6px;line-height:22px;color:#333}
.footer{left:0;top:1362px;width:1200px;height:86px;background:var(--navy);border-top:3px solid #9aa0aa}
.flinks{left:108px;top:1393px;font-family:Arial,sans-serif;font-size:14px;color:#fff;display:flex;gap:0;white-space:nowrap}
.flinks span{margin-right:21px}
.flinks .on{color:var(--orange)}
.connect{left:837px;top:1393px;font-family:Arial,sans-serif;font-size:14px;color:var(--orange)}
.social{top:1389px;width:22px;height:22px;background:#dfe3ea;border-radius:2px}
</style>
</head>
<body>
<div class="page">
  <div class="abs hero" role="img" aria-label="Photograph of a smiling businessman in a suit with colleagues in an office behind him"></div>
  <div class="abs topbar"></div>
  <div class="abs topline"></div>

  <div class="abs logo-box"><span class="logo-dot"></span><span class="logo-name">Harwood &amp; Beale LLP</span></div>

  <ul class="abs nav">
    <li>HOME</li><li>ABOUT US</li><li>SOLUTIONS</li><li>NEWS</li><li>CAREERS</li><li>CONTACT US</li>
  </ul>

  <div class="abs util"></div>
  <div class="abs search">Search
    <svg width="16" height="16" viewBox="0 0 16 16"><circle cx="6.5" cy="6.5" r="4.5" fill="none" stroke="#1c5fa8" stroke-width="2"/><path d="M10 10l4 4" stroke="#1c5fa8" stroke-width="2.5"/></svg>
  </div>
  <div class="abs phone">
    <svg width="13" height="18" viewBox="0 0 13 18"><path d="M3 1l3 4-2 2c1 2 2 4 4 6l2-2 3 3-2 3C5 16 1 10 1 4z" fill="#1c4f8f"/></svg>
    555-014-2290
  </div>

  <svg class="abs arrow" style="left:62px" width="40" height="52" viewBox="0 0 40 52"><path d="M22 0L4 26l18 26h9L13 26 31 0z" fill="#f47a0c"/><path d="M34 4L18 26l16 22h6L24 26 40 4z" fill="#0d3670"/></svg>
  <svg class="abs arrow" style="left:1098px" width="40" height="52" viewBox="0 0 40 52"><path d="M6 4l16 22L6 48H0l16-22L0 4z" fill="#0d3670"/><path d="M18 0l18 26-18 26H9l18-26L9 0z" fill="#f47a0c"/></svg>

  <div class="abs tagline">
    <h1>A BEAUTIFUL TAG LINE GOES HERE</h1>
    <p>Lorem ipsum dolor sit amet, consectetuer adipiscing elit, sed diam nonummy nibh euismod tincidunt ut laoreet dolore magna aliquam erat volutpat. Ut wisi enim ad minim veniam, quis nostrud exerci tation ullamcorper suscipit lobortis.</p>
  </div>

  <div class="abs features">
    <div class="feature" style="width:255px">
      <svg class="hex" width="62" height="68" viewBox="0 0 62 68"><path d="M31 2l28 16v32L31 66 3 50V18z" fill="#fff" stroke="#1d5fa8" stroke-width="3"/><path d="M20 40v-8a11 11 0 0 1 22 0v8" fill="none" stroke="#f47a0c" stroke-width="2.5"/><rect x="17" y="33" width="7" height="11" rx="2" fill="none" stroke="#f47a0c" stroke-width="2.5"/><rect x="38" y="33" width="7" height="11" rx="2" fill="none" stroke="#f47a0c" stroke-width="2.5"/></svg>
      <h2>HEADING HERE</h2>
      <p>Lorem ipsum dolor sit amet, con-sectetuer adipiscing elit, sed diam nonummy nibh euismod.</p>
      <div class="more-row" style="top:147px"><span class="btn"><svg width="8" height="11" viewBox="0 0 8 11"><path d="M1 0l6 5.5L1 11" fill="none" stroke="#f7931e" stroke-width="2.5"/></svg>More</span></div>
    </div>
    <div class="feature" style="width:247px">
      <svg class="hex" width="62" height="68" viewBox="0 0 62 68"><path d="M31 2l28 16v32L31 66 3 50V18z" fill="#fff" stroke="#1d5fa8" stroke-width="3"/><path d="M20 26a14 14 0 0 0 18 18z" fill="none" stroke="#f47a0c" stroke-width="2.5"/><path d="M29 35l8-8M27 46l-4 5h14l-4-5" fill="none" stroke="#f47a0c" stroke-width="2.5"/></svg>
      <h2>HEADING HERE</h2>
      <p>Lorem ipsum dolor sit amet, con-sectetuer adipiscing elit, sed diam nonummy nibh euismod.</p>
      <div class="more-row" style="top:147px"><span class="btn"><svg width="8" height="11" viewBox="0 0 8 11"><path d="M1 0l6 5.5L1 11" fill="none" stroke="#f7931e" stroke-width="2.5"/></svg>More</span></div>
    </div>
    <div class="feature" style="width:245px">
      <svg class="hex" width="62" height="68" viewBox="0 0 62 68"><path d="M31 2l28 16v32L31 66 3 50V18z" fill="#fff" stroke="#1d5fa8" stroke-width="3"/><rect x="17" y="24" width="28" height="19" fill="none" stroke="#f47a0c" stroke-width="2.5"/><path d="M13 46h36" stroke="#f47a0c" stroke-width="3"/><path d="M27 29l8 4-4 1-1 4z" fill="#f47a0c"/></svg>
      <h2>HEADING HERE</h2>
      <p>Lorem ipsum dolor sit amet, con-sectetuer adipiscing elit, sed diam nonummy nibh euismod.</p>
      <div class="more-row" style="top:147px"><span class="btn"><svg width="8" height="11" viewBox="0 0 8 11"><path d="M1 0l6 5.5L1 11" fill="none" stroke="#f7931e" stroke-width="2.5"/></svg>More</span></div>
    </div>
    <div class="feature" style="width:253px">
      <svg class="hex" width="62" height="68" viewBox="0 0 62 68"><path d="M31 2l28 16v32L31 66 3 50V18z" fill="#fff" stroke="#1d5fa8" stroke-width="3"/><rect x="16" y="27" width="30" height="19" rx="2" fill="none" stroke="#f47a0c" stroke-width="2.5"/><rect x="20" y="31" width="17" height="11" fill="none" stroke="#f47a0c" stroke-width="2"/><path d="M25 20l6 6 6-6" fill="none" stroke="#f47a0c" stroke-width="2.5"/></svg>
      <h2>HEADING HERE</h2>
      <p>Lorem ipsum dolor sit amet, con-sectetuer adipiscing elit, sed diam nonummy nibh euismod.</p>
      <div class="more-row" style="top:147px"><span class="btn"><svg width="8" height="11" viewBox="0 0 8 11"><path d="M1 0l6 5.5L1 11" fill="none" stroke="#f7931e" stroke-width="2.5"/></svg>More</span></div>
    </div>
  </div>

  <div class="abs content"></div>
  <section class="abs main">
    <h2>A Beautiful Heading Goes Here</h2>
    <hr>
    <p>Lorem ipsum dolor sit amet, consectetuer adipiscing elit, sed diam nonummy nibh euismod tinc-idunt ut laoreet dolore magna aliquam erat volutpat. Ut wisi enim ad minim veniam, quis nostrud exerci tation ullamcorper suscipit lobortis nisl ut aliquip ex ea commodo consequat. Duis autem vel eum iriure dolor in hendrerit in vulputate velit esse molestie consequat, vel illum dolore eu feugiat nulla facilisis at vero eros et accumsan et iusto odio dignissim qui blandit praesent lupta-tum zzril delenit augue duis dolore te feugait nulla facilisi.</p>
    <p>Nam liber tempor cum soluta nobis eleifend option congue nihil imperdiet doming id quod mazim placerat facer possim assum. Typi non habent claritatem insitam; est usus legentis in iis qui facit eorum claritatem. Investigationes demonstraverunt lectores legere me lius quod ii legunt saepius.</p>
  </section>

  <section class="abs news">
    <h2>Latest News</h2>
    <div class="date">Tuesday, June 17, 2014</div>
    <p>Lorem ipsum dolor sit amet, consectetuer adipiscing elit, sed diam nonummy nibh euismod tincidunt ut laoreet dolore magna aliquam erat volutpat.</p>
    <div class="date" style="margin-top:21px">Tuesday, June 17, 2014</div>
    <p>Ut wisi enim ad minim veniam, quis nos-trud exerci tation ullamcorper suscipit lobortis nisl ut aliquip ex ea commodo consequat.</p>
  </section>
  <div class="more-row" style="position:absolute;left:810px;width:280px;top:1224px"><span class="btn"><svg width="8" height="11" viewBox="0 0 8 11"><path d="M1 0l6 5.5L1 11" fill="none" stroke="#f7931e" stroke-width="2.5"/></svg>More</span></div>

  <footer class="abs footer"></footer>
  <nav class="abs flinks">
    <span class="on">Home</span><span>/</span><span>About us</span><span>/</span><span>Solutions</span><span>/</span><span>News</span><span>/</span><span>Careers</span><span>/</span><span>Contact us</span>
  </nav>
  <div class="abs connect">Connect with us :</div>
  <span class="abs social" style="left:986px" aria-label="Social link"></span>
  <span class="abs social" style="left:1027px" aria-label="Social link"></span>
  <span class="abs social" style="left:1071px" aria-label="Social link"></span>
</div>
</body>
</html>
```